Willowmere Stud website

We would like to create a horse stud/agistment farm website similar to this websites we have attached below:
www.thornbrae.com.au
www.kestlewood.com.au
www.brindlecote.com
www.fenwaite.com.au
The main colour scheme are purple and white to align with the stable's racing colours.
We have also attach the company logo and also images of the farm and create some ideas for the website.
Many thanks for looking into this project!

```html
<!DOCTYPE html>
<html lang="en">
<head>
<meta charset="utf-8">
<title>Willowmere Stud</title>
<link rel="stylesheet" href="https://fonts.googleapis.com/css2?family=Poppins:wght@400;500;600;700&family=Open+Sans:wght@400;600&display=swap">
<style>
:root{
  --purple:#3d1846;
  --purple-deep:#2b0f33;
  --white:#ffffff;
  --ink:#1d1d1d;
  --text:#5a5a5a;
  --footer:#1a1d1a;
}
*{box-sizing:border-box;margin:0;padding:0}
html,body{width:1200px;height:3673px;overflow:hidden}
body{position:relative;background:var(--white);font-family:"Open Sans",sans-serif;color:var(--text)}
.abs{position:absolute}
.heading{font-family:"Poppins",sans-serif;color:var(--ink);font-weight:600}

/* header */
.site-header{left:0;top:0;width:1200px;height:108px;background:var(--purple);z-index:5}
.brand{left:110px;top:34px;display:flex;align-items:center;gap:14px;color:var(--white);font-family:"Poppins",sans-serif;font-weight:600;font-size:25px;letter-spacing:.5px;white-space:nowrap}
.brand-dot{width:44px;height:44px;border:3px solid var(--white);border-radius:50%}
.main-nav{left:442px;top:47px;display:flex;gap:28px;font-family:"Poppins",sans-serif;font-size:15px;color:var(--white);white-space:nowrap}
.main-nav a{color:inherit;text-decoration:none}
.search-icon{left:1072px;top:50px}

/* hero */
.hero{left:0;top:0;width:1200px;height:713px;background:linear-gradient(180deg,#3b4250 0%,#6f7a86 30%,#c9a777 48%,#5d6a3c 62%,#38471f 100%)}
.hero-title{left:0;top:318px;width:1200px;text-align:center;font-family:"Poppins",sans-serif;font-weight:600;font-size:72px;color:var(--white);letter-spacing:1px}
.hero-sub{left:0;top:422px;width:1200px;text-align:center;font-size:24px;color:var(--white)}
.dots{display:flex;gap:6px}
.dots span{width:15px;height:15px;border-radius:50%;border:2px solid var(--white)}
.dots span.on{background:var(--white)}
.hero .dots{position:absolute;left:564px;top:612px}

/* welcome */
.welcome-title{left:0;top:812px;width:1200px;text-align:center;font-size:43px;letter-spacing:.5px}
.welcome-text{left:220px;top:896px;width:760px;text-align:center;font-size:14px;line-height:32px}

/* services */
.services{left:0;top:1053px;width:1200px;height:661px;background:linear-gradient(180deg,#3d4a33 0%,#2d3a22 45%,#3f5a26 75%,#263618 100%)}
.service-photo{width:220px;height:220px;border-radius:50%;border:6px solid var(--white)}
.service-title{width:270px;text-align:center;font-family:"Poppins",sans-serif;font-weight:600;font-size:20px;line-height:33px;color:var(--white);white-space:nowrap}
.service-text{width:230px;text-align:center;font-size:13px;line-height:27px;color:var(--white)}

/* news */
.news-title{left:110px;top:1798px;font-size:40px}
.news-photo{width:272px;height:194px}
.news-card-title{font-family:"Poppins",sans-serif;font-weight:500;font-size:21px;color:var(--ink);white-space:nowrap}
.news-meta{font-size:14px;color:#444;display:flex;align-items:center;gap:8px;white-space:nowrap}
.news-text{width:272px;font-size:13.5px;line-height:27px}
.btn-outline{width:140px;height:46px;border:2.5px solid var(--purple);border-radius:23px;font-family:"Poppins",sans-serif;font-weight:600;font-size:14px;color:var(--ink);display:flex;align-items:center;justify-content:center}
.grass-strip{left:0;top:2388px;width:1200px;height:73px;background:linear-gradient(180deg,#7fb33c,#4d8a22)}

/* videos */
.videos-title{left:0;top:2546px;width:1200px;text-align:center;font-size:40px}
.videos-text{left:220px;top:2630px;width:760px;text-align:center;font-size:14px;line-height:32px}
.video-frame{left:348px;top:2743px;width:504px;height:348px;border:5px solid var(--white);box-shadow:0 0 0 1px #ddd;background:linear-gradient(180deg,#4a3a2a 0%,#7b6548 40%,#3f7a2c 70%,#c45b5b 88%,#2f6a26 100%);z-index:3}
.play{left:215px;top:137px;width:64px;height:64px}
.arrow-btn{width:58px;height:58px;border-radius:50%;border:2px solid #bbb;background:var(--white)}

/* footer */
.site-footer{left:0;top:3040px;width:1200px;height:633px;background:linear-gradient(180deg,#2a3326 0%,#181c17 40%,#141714 100%)}
.footer-head{font-family:"Poppins",sans-serif;font-weight:500;font-size:22px;color:var(--white)}
.field{height:32px;background:var(--white);font-size:11px;color:#777;padding:8px 10px}
.btn-solid{width:118px;height:46px;border-radius:23px;background:var(--purple);color:var(--white);font-family:"Poppins",sans-serif;font-weight:600;font-size:14px;display:flex;align-items:center;justify-content:center}
.info-row{left:789px;display:flex;align-items:flex-start;gap:28px;font-size:14px;line-height:24px;color:var(--white);white-space:nowrap}
.info-icon{width:38px;height:38px;border-radius:50%;border:2px solid var(--white);flex:none;display:flex;align-items:center;justify-content:center}
.divider{left:110px;top:3563px;width:980px;height:1px;background:rgba(255,255,255,.25)}
.copyright{left:110px;top:3605px;font-size:14px;color:var(--white)}
.social{width:40px;height:40px;border-radius:50%;border:2px solid var(--white)}
</style>
</head>
<body>

<section class="hero abs" role="img" aria-label="Photograph of farm paddocks with timber fences under a cloudy evening sky">
  <div class="dots"><span class="on"></span><span></span><span></span><span></span></div>
</section>
<h1 class="hero-title abs">WILLOWMERE STUD</h1>
<p class="hero-sub abs">Nam libero tempocum soluta nobis est eligendi</p>

<header class="site-header abs">
  <div class="brand abs"><span class="brand-dot"></span>WILLOWMERE STUD</div>
  <nav class="main-nav abs">
    <a>Home</a><a>About us</a><a>News</a><a>Stallions</a><a>Farm</a><a>Gallery</a><a>Sales</a><a>Contact</a>
  </nav>
  <svg class="search-icon abs" width="16" height="16" viewBox="0 0 16 16"><circle cx="6.5" cy="6.5" r="5" fill="none" stroke="#fff" stroke-width="2"/><line x1="10" y1="10" x2="15" y2="15" stroke="#fff" stroke-width="2"/></svg>
</header>

<h2 class="welcome-title heading abs">WELCOME TO WILLOWMERE STUD</h2>
<p class="welcome-text abs">Nam libero tempore, cum soluta nobis est eligendi optio cumque nihil impedit quo minus id quod maxime plac eat facere possimus, omnis voluptas assumenda est, omnis dolor repellen ribus autem quibusdam et aut officiis debitis aut rerum necessitatibus saepe eveniet ut et voluptates repudiandae sint et mole</p>

<section class="services abs" role="img" aria-label="Photograph of a green grass paddock with trees"></section>
<svg class="abs" style="left:0;top:1053px" width="1200" height="240" viewBox="0 0 1200 240">
  <path d="M0 0 H1200 V200 Q600 30 0 215 Z" fill="#fff"/>
  <path d="M0 215 Q600 30 1200 200" fill="none" stroke="#3d1846" stroke-width="12"/>
</svg>
<div class="service-photo abs" style="left:110px;top:1122px;background:linear-gradient(160deg,#d9c9a4,#8a7a55 60%,#4f6a2e)" role="img" aria-label="Palomino stallion head portrait"></div>
<div class="service-photo abs" style="left:363px;top:1066px;background:linear-gradient(160deg,#7a9a4a,#6b4526 55%,#4b6f2a)" role="img" aria-label="Bay horse standing in a paddock"></div>
<div class="service-photo abs" style="left:615px;top:1066px;background:linear-gradient(160deg,#9ab85a,#6e4a2a 55%,#5a8a30)" role="img" aria-label="Young horse being shown on grass"></div>
<div class="service-photo abs" style="left:865px;top:1122px;background:linear-gradient(160deg,#5a6a8a,#a0a0a8 50%,#5a3a6a)" role="img" aria-label="Grey horse with jockey in purple silks at a racecourse"></div>

<h3 class="service-title abs" style="left:85px;top:1380px">Silver Tamarind<br>(USA)</h3>
<p class="service-text abs" style="left:105px;top:1456px">Silver Tamarind (USA). Double dilute thoroughbred stallion, guaranteed palomino or buckskin. Available for live cover and for frozen/chilled semen later this season.</p>
<h3 class="service-title abs" style="left:338px;top:1322px">Re-education of<br>problem horses</h3>
<p class="service-text abs" style="left:358px;top:1400px">At vero eos et accusamus et iu sto odio dignissimos ducimus qui blanditiis praesentium voluptatum deleniti atque corrupti quos do lores bero tempore</p>
<h3 class="service-title abs" style="left:590px;top:1322px">Weanling and Yearling<br>Sales Preparation</h3>
<p class="service-text abs" style="left:610px;top:1400px">At vero eos et accusamus et iu sto odio dignissimos ducimus qui blanditiis praesentium voluptatum deleniti atque corrupti quos do lores bero tempore</p>
<h3 class="service-title abs" style="left:840px;top:1380px">Facility<br>hire</h3>
<p class="service-text abs" style="left:860px;top:1456px">Indoor Arena, Outdoor Arena and various sized rubbered round yards both indoor and outdoor</p>
<div class="dots abs" style="left:584px;top:1618px"><span class="on"></span><span></span></div>

<h2 class="news-title heading abs">RECENT NEWS</h2>
<div class="news-photo abs" style="left:110px;top:1900px;background:linear-gradient(180deg,#6f9ac6 0%,#7fa35a 35%,#4f7a2c 100%)" role="img" aria-label="Aerial view of stud buildings and paddocks"></div>
<div class="news-photo abs" style="left:419px;top:1900px;background:linear-gradient(180deg,#8d96a3 0%,#6f7a5a 40%,#3f6a26 100%)" role="img" aria-label="Horses grazing in a paddock"></div>

<h3 class="news-card-title abs" style="left:110px;top:2122px">Finibus Bonoret Malor</h3>
<div class="news-meta abs" style="left:114px;top:2166px">
  <svg width="13" height="13" viewBox="0 0 13 13"><rect x="1" y="2" width="11" height="10" fill="none" stroke="#444" stroke-width="1.5"/><line x1="1" y1="5" x2="12" y2="5" stroke="#444" stroke-width="1.5"/></svg>07/03/2019 &nbsp;|&nbsp;
  <svg width="12" height="13" viewBox="0 0 12 13"><circle cx="6" cy="4" r="3" fill="#444"/><path d="M0 13 Q6 5 12 13Z" fill="#444"/></svg>John
</div>
<p class="news-text abs" style="left:110px;top:2204px">Nam libero tempore, cum soluta nobiest eligendi optio cumque nihil impedit qimi nus id quod maxime plac.</p>
<div class="btn-outline abs" style="left:112px;top:2312px">READ MORE</div>

<h3 class="news-card-title abs" style="left:419px;top:2122px">Finibus Bonoret Malor</h3>
<div class="news-meta abs" style="left:423px;top:2166px">
  <svg width="13" height="13" viewBox="0 0 13 13"><rect x="1" y="2" width="11" height="10" fill="none" stroke="#444" stroke-width="1.5"/><line x1="1" y1="5" x2="12" y2="5" stroke="#444" stroke-width="1.5"/></svg>07/03/2019 &nbsp;|&nbsp;
  <svg width="12" height="13" viewBox="0 0 12 13"><circle cx="6" cy="4" r="3" fill="#444"/><path d="M0 13 Q6 5 12 13Z" fill="#444"/></svg>John
</div>
<p class="news-text abs" style="left:419px;top:2204px">Nam libero tempore, cum soluta nobiest eligendi optio cumque nihil impedit qimi nus id quod maxime plac.</p>
<div class="btn-outline abs" style="left:421px;top:2312px">READ MORE</div>

<div class="grass-strip abs" role="img" aria-label="Strip of green grass"></div>
<div class="abs" style="left:710px;top:1837px;width:490px;height:612px;background:linear-gradient(90deg,rgba(255,255,255,0) 0%,rgba(40,30,28,.85) 25%,rgba(110,60,35,.9) 65%,rgba(255,255,255,0) 100%);border-radius:40% 40% 10% 10%" role="img" aria-label="Two horses, one black and one chestnut, standing side by side"></div>

<h2 class="videos-title heading abs">VIDEOS</h2>
<p class="videos-text abs">Nam libero tempore, cum soluta nobis est eligendi optio cumque nihil impedit quo minus id quod maxime plac eat facere possimus, omnis voluptas assumenda est, omnis dolor repellen ribus autem.</p>

<footer class="site-footer abs" role="img" aria-label="Dim photograph of paddocks at dusk"></footer>
<svg class="abs" style="left:0;top:2990px" width="1200" height="140" viewBox="0 0 1200 140">
  <path d="M0 0 H1200 V130 Q600 -20 0 130 Z" fill="#fff"/>
  <path d="M0 132 Q600 -18 1200 132" fill="none" stroke="#3d1846" stroke-width="14"/>
</svg>

<div class="video-frame abs" role="img" aria-label="Video still of a grey racehorse and jockey in purple silks">
  <svg class="play abs" viewBox="0 0 64 64"><circle cx="32" cy="32" r="32" fill="rgba(0,0,0,.6)"/><path d="M25 19 L47 32 L25 45Z" fill="#fff"/></svg>
</div>
<svg class="arrow-btn abs" style="left:218px;top:2883px" viewBox="0 0 58 58"><path d="M33 19 L23 29 L33 39" fill="none" stroke="#888" stroke-width="2.5"/></svg>
<svg class="arrow-btn abs" style="left:921px;top:2883px" viewBox="0 0 58 58"><path d="M25 19 L35 29 L25 39" fill="none" stroke="#888" stroke-width="2.5"/></svg>

<h3 class="footer-head abs" style="left:110px;top:3208px">Contact Us</h3>
<div class="field abs" style="left:112px;top:3282px;width:312px">First Name</div>
<div class="field abs" style="left:431px;top:3282px;width:311px">Last Name</div>
<div class="field abs" style="left:112px;top:3326px;width:312px">Email</div>
<div class="field abs" style="left:431px;top:3326px;width:311px">Phone Number</div>
<div class="field abs" style="left:112px;top:3375px;width:630px;height:81px">Comments</div>
<div class="btn-solid abs" style="left:112px;top:3473px">SUBMIT</div>

<h3 class="footer-head abs" style="left:789px;top:3208px">Contact Information</h3>
<div class="info-row abs" style="top:3274px">
  <span class="info-icon"><svg width="12" height="16" viewBox="0 0 12 16"><path d="M6 0 A6 6 0 0 1 12 6 C12 10 6 16 6 16 C6 16 0 10 0 6 A6 6 0 0 1 6 0Z" fill="#fff"/><circle cx="6" cy="6" r="2.2" fill="#1a1d1a"/></svg></span>
  <span>48 Hollins Creek Rd<br>Merriwa NSW 2329</span>
</div>
<div class="info-row abs" style="top:3346px">
  <span class="info-icon"><svg width="14" height="14" viewBox="0 0 14 14"><path d="M3 0 L5 4 L3.5 5.5 Q5 8.5 8.5 10.5 L10 9 L14 11 L12.5 14 Q5 13 0 2Z" fill="#fff"/></svg></span>
  <span style="padding-top:6px">1 800 555 0142</span>
</div>
<div class="info-row abs" style="top:3402px">
  <span class="info-icon"><svg width="15" height="11" viewBox="0 0 15 11"><rect width="15" height="11" fill="#fff"/><path d="M0 0 L7.5 6 L15 0" fill="none" stroke="#1a1d1a" stroke-width="1.5"/></svg></span>
  <span style="padding-top:6px">info@willowmerestud.com</span>
</div>
<div class="info-row abs" style="top:3461px">
  <span class="info-icon"><svg width="16" height="16" viewBox="0 0 16 16"><circle cx="8" cy="8" r="7" fill="#fff"/><path d="M1 8 H15 M8 1 Q4 8 8 15 M8 1 Q12 8 8 15" fill="none" stroke="#1a1d1a" stroke-width="1"/></svg></span>
  <span style="padding-top:6px">www.willowmerestud.com</span>
</div>

<div class="divider abs"></div>
<p class="copyright abs">Copyright © 2019, Willowmere Stud. All right reserved</p>
<span class="social abs" style="left:957px;top:3596px" aria-label="Social link"></span>
<span class="social abs" style="left:1003px;top:3596px" aria-label="Social link"></span>
<span class="social abs" style="left:1048px;top:3596px" aria-label="Social link"></span>

</body>
</html>
```